Gaming Convention Stand Up Banners

I need 3 different designs for our banners at ArcadiaCon. Our company is running a board game area, LAN area, and our general booth space that is for advertising our LAN/Gaming center. These banner stands are 71" tall by 31" wide.
The board game and LAN banners should say "Board Games" or "LAN" and say free play or come and play or something indicating that people can come and play games for free. It is fine to show art from games on these banners. I'll include some example games at the bottom for each area.
The booth banner should have the Seeking a Squad logo (included in uploaded files) and say that we offer Game Time Rental, Parties, Tournaments, and More. (See www.qvtkel.com for our website).
I included the two that we made for Arcadia last year. I'm not a good designer, so I was hoping for something more eye catching and cool for this year. I would like all three to look like they're part of a set.
Board Games that we will be showing:
Moonhowl
Seeding Venus Prime
Pioneers of Brelund
Phantom Dusk Hour
Kozuki
Clock Fables
LAN Games that we will be showing:
Vox Arcana
Brawlor 4
Pippo Racer
Goose Brawl
Skarvel
Vortex Arena 2001
Gloom
Dominionship
Alley Brawler
Harbor Town Heist
Target Market(s)
Gaming show attendees
Industry/Entity Type
Games
Font styles to use
Other font styles liked:
- Andale Mono is our logo typeface, but I'm happy with whatever
Colors
Designer to choose colors to be used in the design.
Requirements
Must have
- Three 71x31 designs, one for each area of the show floor. (LAN, Board Games, Info Booth)
Nice to have
- Lan/Board Games -> Free to play, invitations to come play
- Info -> Info from www.qvtkel.com website, or facebook.com/qvtkel
Should not have
- Sexually suggestive content (this is a family friendly event)
- Content too low (these are floor standing, the bottom 2 feet are a little hard to read)

```html
<!DOCTYPE html>
<html lang="en">
<head>
<meta charset="utf-8">
<title>Board Games Free Play Banner</title>
<link href="https://fonts.googleapis.com/css2?family=Lato:wght@400;700;900&family=Arimo:wght@700&display=swap" rel="stylesheet">
<style>
  :root {
    --page-bg: #e9eaec;
    --sky-top: #8fcbe6;
    --sky-mid: #a9c9c9;
    --hill-green: #3e5a3a;
    --brand-blue: #0a7cc9;
    --deep-blue: #0b73c0;
    --brand-green: #5aa57e;
    --soft-white: #f7f7f7;
    --ink: #1b1b1b;
  }
  * { margin: 0; padding: 0; box-sizing: border-box; }
  html, body { width: 1200px; height: 1200px; overflow: hidden; background: var(--page-bg); }
  body { font-family: "Lato", sans-serif; position: relative; }

  .banner {
    position: absolute; left: 380px; top: 40px;
    width: 440px; height: 1120px;
    background: linear-gradient(180deg, #ffffff 0%, #f1f1f1 100%);
    overflow: hidden;
    box-shadow: 0 6px 24px rgba(0,0,0,0.12);
  }
  .hero { position: absolute; left: 0; top: 0; width: 440px; height: 620px; }

  .brand-circle {
    position: absolute; left: 24px; top: 465px;
    width: 200px; height: 200px; border-radius: 50%;
    background: #ffffff; border: 3px solid var(--brand-blue);
    display: flex; align-items: center; justify-content: center; text-align: center;
  }
  .brand-name {
    font-weight: 900; font-size: 26px; line-height: 1.1;
    color: var(--brand-blue); width: 150px;
  }

  .free-badge {
    position: absolute; left: 298px; top: 505px;
    width: 122px; height: 122px; border-radius: 50%;
    background: var(--brand-green); border: 3px solid var(--brand-blue);
    display: flex; flex-direction: column; align-items: center; justify-content: center;
    font-family: "Arimo", sans-serif; font-weight: 700; line-height: 1;
  }
  .free-badge .free { color: #ffffff; font-size: 34px; }
  .free-badge .play { color: var(--ink); font-size: 32px; margin-top: 4px; }

  .section-title {
    position: absolute; left: 0; width: 440px; top: 690px; text-align: center;
    font-family: "Arimo", sans-serif; font-weight: 700; font-size: 24px;
    color: var(--brand-green); text-decoration: underline; text-underline-offset: 3px;
  }

  .game-list { position: absolute; list-style: none; font-size: 19px; font-weight: 700; color: var(--ink); }
  .game-list li { position: relative; padding-left: 26px; }
  .game-list li::before {
    content: ""; position: absolute; left: 2px; top: 9px;
    width: 8px; height: 8px; border-radius: 50%;
  }
  .game-list--left { left: 34px; top: 748px; }
  .game-list--left li { height: 45px; }
  .game-list--left li::before { background: var(--brand-green); }
  .game-list--right { left: 272px; top: 738px; }
  .game-list--right li { height: 43px; }
  .game-list--right li::before { background: var(--brand-blue); }

  .contact-band { position: absolute; left: 0; top: 935px; width: 440px; height: 185px; }

  .character {
    position: absolute; left: 320px; top: 812px; width: 118px; height: 185px;
    background: radial-gradient(ellipse at 50% 45%, #7a4a8e 0%, #3a66b8 55%, rgba(40,60,110,0) 78%);
    border-radius: 40% 40% 20% 20%;
  }

  .contact-title {
    position: absolute; left: 34px; top: 970px;
    font-weight: 700; font-size: 25px; color: #ffffff; text-decoration: underline;
    text-underline-offset: 3px;
  }
  .contact-item {
    position: absolute; display: flex; align-items: flex-start; gap: 7px;
    color: #ffffff; font-size: 15px; line-height: 1.3;
  }
  .contact-item svg { flex: none; margin-top: 1px; }
  .contact-phone { left: 34px; top: 1016px; }
  .contact-email { left: 34px; top: 1056px; }
  .contact-address { left: 222px; top: 1004px; }
  .contact-web { left: 222px; top: 1046px; }
</style>
</head>
<body>
  <main class="banner">
    <svg class="hero" viewBox="0 0 440 620" width="440" height="620">
      <defs>
        <linearGradient id="sceneGrad" x1="0" y1="0" x2="0" y2="1">
          <stop offset="0" stop-color="var(--sky-top)"/>
          <stop offset="0.45" stop-color="var(--sky-mid)"/>
          <stop offset="0.7" stop-color="#6f8c78"/>
          <stop offset="1" stop-color="var(--hill-green)"/>
        </linearGradient>
      </defs>
      <rect role="img" aria-label="Sci-fi scene of floating alien ships above a mountain and green forested hills" x="0" y="0" width="440" height="620" fill="url(#sceneGrad)"/>
      <path d="M0 470 Q30 540 120 560 L300 555 Q400 540 440 470 L440 620 L0 620 Z" fill="#ffffff"/>
      <path d="M0 470 Q30 540 120 560" fill="none" stroke="var(--brand-green)" stroke-width="6"/>
      <path d="M0 470 Q30 540 120 560" fill="none" stroke="var(--brand-blue)" stroke-width="2"/>
      <path d="M200 560 L300 555 Q400 540 440 470" fill="none" stroke="var(--brand-green)" stroke-width="6"/>
      <path d="M200 560 L300 555 Q400 540 440 470" fill="none" stroke="var(--brand-blue)" stroke-width="2"/>
    </svg>

    <div class="brand-circle"><span class="brand-name">Seeking a Squad</span></div>

    <div class="free-badge"><span class="free">FREE</span><span class="play">play</span></div>

    <h1 class="section-title">Board Games</h1>

    <ul class="game-list game-list--left">
      <li>Moonhowl</li>
      <li>Seeding Venus Prime</li>
      <li>Pioneers of Brelund</li>
      <li>Phantom Dusk Hour</li>
    </ul>
    <ul class="game-list game-list--right">
      <li>Kozuki</li>
      <li>Clock Fables</li>
    </ul>

    <svg class="contact-band" viewBox="0 0 440 185" width="440" height="185">
      <path d="M0 28 L440 0 L440 185 L0 185 Z" fill="var(--deep-blue)"/>
      <path d="M0 26 L440 -2" stroke="var(--brand-green)" stroke-width="4"/>
    </svg>

    <div class="character" role="img" aria-label="Muscular blue game character illustration"></div>

    <h2 class="contact-title">CONTACT US</h2>

    <div class="contact-item contact-phone">
      <svg width="16" height="16" viewBox="0 0 16 16"><circle cx="8" cy="8" r="8" fill="#ffffff" opacity="0.85"/><path d="M5 4 L7 4 L7.5 6.5 L6.5 7.2 Q7.5 9 9 9.8 L9.8 8.6 L12 9.2 L12 11 Q8 12 5 8 Z" fill="var(--deep-blue)"/></svg>
      <span>(555) 318-2740</span>
    </div>
    <div class="contact-item contact-email">
      <svg width="16" height="16" viewBox="0 0 16 16"><circle cx="8" cy="8" r="8" fill="#ffffff" opacity="0.85"/><rect x="4" y="5" width="8" height="6" fill="none" stroke="var(--deep-blue)" stroke-width="1.2"/><path d="M4 5 L8 8.5 L12 5" fill="none" stroke="var(--deep-blue)" stroke-width="1.2"/></svg>
      <span>owners@qvtkel.com</span>
    </div>
    <div class="contact-item contact-address">
      <svg width="16" height="18" viewBox="0 0 16 18"><path d="M8 1 A6 6 0 0 1 14 7 C14 11 8 17 8 17 C8 17 2 11 2 7 A6 6 0 0 1 8 1 Z" fill="#ffffff"/><circle cx="8" cy="7" r="2.2" fill="var(--deep-blue)"/></svg>
      <span>417 Larkspur Ave<br>Millbrook, PA 15099</span>
    </div>
    <div class="contact-item contact-web">
      <svg width="16" height="16" viewBox="0 0 16 16"><circle cx="8" cy="8" r="7" fill="none" stroke="#ffffff" stroke-width="1.4"/><path d="M1 8 H15 M8 1 Q4 8 8 15 M8 1 Q12 8 8 15" fill="none" stroke="#ffffff" stroke-width="1.1"/></svg>
      <span>www.qvtkel.com</span>
    </div>
  </main>
</body>
</html>
```